Prime Loom Events: A Strategic Event Planning Company Website
A focus on events. All of them. All aspects of them. Anywhere.
Prime Loom Events:  A Strategic Event Planning Company Website - Events
Creative Brief
Events
www.primeloomevents-demo.com
We are an event company. We handle all sorts of events in all sorts of locations.
We handle the fun events but we excel at strategic events. We surpass our competition by not only mastering the details but balancing them within the larger strategic picture. We differentiate ourselves through our passionate, positive service. We partner with our clients and their teams. We become a part of their team. And, perhaps most importantly, we become as invested in the event’s success as they are.
A Philosophy
In the 1950’s, doctors developed a personality classification that was supposed to help them identify predicators for heart disease. They grouped certain criteria together and labeled that personality, “Type A”. The term has come to have some negative connotations.
From our point of view, while we are an eclectic team of varied personalities and interests, we endeavor to provide type A service.
Does that make us a group of unlikable, over-bearing maniacs? No.
We think the so-called “symptoms” of type A are the same qualifications you want in your event planners:
Type A individuals can be described as time-conscious, competitive, ambitious, business-like perfectionists. They are usually over-achievers who derive a great deal of satisfaction from work and multi-tasking. They drive themselves with deadlines and are often “stress junkies”.
–Restless Minds: Their Origins and Remedies, Osric Pellworth
We proudly don the scarlet letter as a badge of our undying need to deliver services to you on time, in budget, and beyond your expectations. If that ends up leading to heart disease….well, we’ll live with that. If our service prevents your heart attacks, then we’ve done our job.
A Focus
There are differing opinions regarding whether the superior term these days is “event planner” or “meeting planner” or any of the other euphemisms.
We’ve settled that debate amongst ourselves and have gone with “event planning”. Meetings are events. Conferences are events. Galas and fundraisers, Incentive Trips, Employee Appreciation, Grand Openings, Sales Meetings, City-Wide Conventions….be they for 10 people or 10,000…are all events.
They are all experiences that should provide a lasting impact for the attendees and value for the stakeholders. (So, we could call ourselves “experience planners” but that’s a little fruity-sounding…even for us.)
We focus on events. All of them. All aspects of them. Anywhere.
We are experts in the development of new events, the re-invention of existing events, and the increased success of proven events. We partner with you and your team to elevate your events from a money-suck to a bona fide company investment with return. Sure, we manage all of the details along the way, but even more so, we help you make it along the way. We provide guidance and direction for your team—whether we are handling one aspect or the entire event
We don’t do widgets. We don’t deal in whatcha-may-call-its. We do events. And, cliché as it is, we do them really well.
A Rundown
Want more specifics about what we offer? We are happy to provide more detailed descriptions on any of our service offerings once we learn what is most applicable to your event.
The services we offer are based on our expertise. We aren’t lawyers. We don’t perform surgery. We aren’t an ad agency. While events fall under headings like public relations and marketing, we don’t claim to be experts in those either. We know events—with all of their related elements—and that is what we sell.
Our services can be modular or comprehensive. Here’s the A to Z (we couldn’t resist including that reference in here somewhere!) of what we offer:
A. Event Development
a. Stakeholder identification
a. Objective and metric setting
a. Event strategy definition
a. ROI Analysis
A. Budgeting
a. Financial projections and reporting
a. Expense tracking and oversight
a. Negotiated savings tracking
A. Project Management
a. Project plan and timeline development/implementation
a. Key performance indicators
a. Project meetings and updates
A. Site Selection
a. Destination analysis
a. Cost comparison
a. Site visits
A. Contract Negotiation
a. Hotel/convention center contracts
a. Vendor and supplier contracts
a. Event risk analysis and mitigation
A. Logistics Management
a. Event Planning
a. Registration
a. Housing/Room block management
(Logistics Management Continued…)
a. Audio-Visual and production management
a. Food and beverage management
a. Transportation
a. Offsite events
a. Theme and décor
a. Meeting room management
a. Venue communication and spec tracking
A. Content Management
a. Speaker procurement and contracting
a. Session development
a. Calls for papers/presentation
a. Speaker and presentation management
a. Session evaluation
a. Session technologies; audience response
A. Event Marketing
a. Marketing plan development
a. Printed, electronic, and web marketing
a. Attendee communications
a. Onsite signage and branding opportunities
A. Revenue and Partner Management
a. Sponsorship and exhibit programs
a. Sponsorship and exhibit sales
a. Tradeshow Management
a. Sponsor/exhibitor communications
A. Onsite Management
Brass Crew
No gold chains or Mr. Q’s here but we do think we’ve got the “Brass Crew” when it comes to talent and service. And, we certainly have set a gold standard for a strong team environment. When you work with us, you’re paired with experienced event managers who meet your needs and your culture. That primary team is supported by an equally dedicated team of expertise that furthers your projects behind the scenes or is drawn on as your project requires.
When you partner with us, you’re not hiring a mom-and-pop shop that can’t maintain your needs. You’re also not turning yourself over to a monstrous event-machine whose strict policies and procedures prevent the adaptability and customization your needs require.
The “Brass Crew” is comprised of highly enthusiastic and talented individuals with such varied backgrounds as: art, business-management, financial management, education, marketing, advertising, graphic and web design, sales, customer service, and, of course, event design, event marketing, and event planning. We are professionals with passion and personality.

```html
<!DOCTYPE html>
<html lang="en">
<head>
<meta charset="utf-8">
<title>Prime Loom Events</title>
<link rel="stylesheet" href="https://fonts.googleapis.com/css2?family=Arimo:wght@400;700&family=Didact+Gothic&display=swap">
<style>
:root{
  --page-bg:#ecedeb;
  --olive:#6d6b3c;
  --olive-dark:#58572f;
  --olive-light:#8b894f;
  --ink:#1d1d1b;
  --muted:#6f6f6f;
  --navy:#163d63;
  --teal-top:#16597d;
  --teal-bottom:#0a2c45;
  --form-grey:#8c8c8a;
  --white:#ffffff;
}
*{box-sizing:border-box;margin:0;padding:0}
html,body{width:1200px;height:942px;overflow:hidden}
body{background:var(--page-bg);font-family:"Arimo",Arial,sans-serif;color:var(--ink);position:relative}
.site{position:absolute;left:185px;top:0;width:820px;height:942px;background:var(--white)}
.abs{position:absolute}

/* header */
.header{left:0;top:0;width:820px;height:127px;background:var(--white)}
.brand{left:42px;top:24px;width:110px;display:flex;flex-direction:column;align-items:center;gap:8px}
.brand-mark{width:52px;height:52px;background:var(--olive)}
.brand-name{font-family:"Didact Gothic",Arial,sans-serif;font-size:13px;color:var(--olive-dark);letter-spacing:.5px;white-space:nowrap}
.tagline{left:178px;top:62px;font-family:"Didact Gothic",Arial,sans-serif;font-size:21px;color:var(--ink);white-space:nowrap}
.contact-line{display:flex;align-items:center;gap:12px;font-size:13px;color:var(--ink);white-space:nowrap}
.contact-email{left:548px;top:40px}
.contact-phone{left:548px;top:80px;font-weight:700;font-size:17px}

/* nav */
.nav{left:0;top:127px;width:820px;height:35px;background:linear-gradient(var(--olive-light),var(--olive-dark));display:flex;align-items:center}
.nav a{color:var(--white);text-decoration:none;font-size:12px;font-weight:700;padding:0 0 0 22px;width:125px}

/* hero */
.hero{left:0;top:162px;width:820px;height:213px;background:linear-gradient(180deg,#c8c2b6 0%,#8a6e5c 40%,#6a3a36 70%,#4a4040 100%)}

/* services */
.services{left:0;top:375px;width:820px;height:288px;background:linear-gradient(var(--olive) 0 118px,var(--white) 118px)}
.service{top:0;width:210px}
.service h2{display:flex;align-items:center;gap:8px;height:48px;font-family:"Didact Gothic",Arial,sans-serif;font-weight:400;font-size:18px;color:var(--white);padding-left:6px;white-space:nowrap}
.service h2 i{width:14px;height:14px;background:var(--olive-light);border:1px solid #c9c79c}
.service-photo{width:210px;height:130px;border:4px solid var(--white);box-shadow:0 1px 3px rgba(0,0,0,.4)}
.service p{margin-top:10px;font-size:10.5px;line-height:14px;color:var(--muted);text-align:justify}
.read-more{display:block;margin:8px 0 0 auto;width:78px;height:18px;background:var(--navy);color:var(--white);font-size:10.5px;font-weight:700;line-height:18px;text-align:center}

/* capabilities band */
.band{left:0;top:663px;width:820px;height:203px;background:linear-gradient(var(--teal-top),var(--teal-bottom))}
.offer{top:22px;color:var(--white)}
.offer h3{display:flex;align-items:center;gap:8px;font-family:"Didact Gothic",Arial,sans-serif;font-weight:400;font-size:18px;margin-bottom:8px;white-space:nowrap}
.offer h3 i{width:14px;height:14px;background:#d8d8d0}
.offer li{list-style:none;font-size:11px;line-height:15px;white-space:nowrap}

.contact-form{left:565px;top:15px;width:242px;height:170px;background:var(--form-grey);border:1px solid #b5b5b3;padding:6px 12px}
.contact-form h4{font-family:"Didact Gothic",Arial,sans-serif;font-weight:400;font-size:17px;color:var(--white);text-align:center;margin-bottom:8px}
.field{display:flex;align-items:center;margin-bottom:8px;font-size:11px;font-weight:700;color:var(--white)}
.field span{width:58px}
.field b{display:block;width:155px;height:17px;background:var(--white)}
.field.message{align-items:flex-start}
.field.message b{height:44px}
.send{margin-left:90px;width:70px;height:18px;background:var(--navy);color:var(--white);font-size:11px;font-weight:700;line-height:18px;text-align:center}

/* footer */
.footer{left:0;top:866px;width:820px;height:76px;background:var(--olive)}
.footer-links{left:20px;top:20px;font-size:11px;color:var(--white)}
.copyright{left:20px;top:40px;font-size:10.5px;color:var(--white)}
</style>
</head>
<body>
<div class="site">
  <header class="header abs">
    <div class="brand abs"><span class="brand-mark"></span><span class="brand-name">PRIME LOOM EVENTS</span></div>
    <div class="tagline abs">Events With a purpose and a result</div>
    <div class="contact-line contact-email abs">
      <svg width="18" height="13" viewBox="0 0 18 13"><rect x="0.5" y="0.5" width="17" height="12" fill="#1d1d1b"/><path d="M1 1l8 6 8-6" stroke="#fff" stroke-width="1.4" fill="none"/></svg>
      <span>inquiries@primeloomevents-demo.com</span>
    </div>
    <div class="contact-line contact-phone abs">
      <svg width="14" height="20" viewBox="0 0 14 20"><path d="M3 1c-2 1-3 3-2 7s4 9 7 11c2 1 4 0 5-1l-3-4-2 1C6 13 5 10 5 8l2-1L5 1z" fill="#1d1d1b"/></svg>
      <span>555.014.2290</span>
    </div>
  </header>

  <nav class="nav abs">
    <a href="#">Home</a><a href="#">About us</a><a href="#">Our Services</a><a href="#">Press Room</a><a href="#">Contact us</a><a href="#">Sitemap</a>
  </nav>

  <div class="hero abs" role="img" aria-label="Photo of a large conference hall filled with attendees at round tables"></div>

  <section class="services abs">
    <div class="service abs" style="left:38px">
      <h2><i></i>Event Development</h2>
      <div class="service-photo" role="img" aria-label="Photo of a production control desk with monitors" style="background:linear-gradient(160deg,#3b4a6a,#1a2235 60%,#5a4a3a)"></div>
      <p>Lorem Ipsum is simply dummy text of the printing and typesetting industry. Lorem Ipsum has been the industry's standard</p>
      <span class="read-more">Read More &gt;&gt;</span>
    </div>
    <div class="service abs" style="left:304px">
      <h2><i></i>Budgeting</h2>
      <div class="service-photo" role="img" aria-label="Photo of a banquet room set with round tables" style="background:linear-gradient(170deg,#b9a48a,#7b4a3a 55%,#d9d3c7)"></div>
      <p>Lorem Ipsum is simply dummy text of the printing and typesetting industry. Lorem Ipsum has been the industry's standard</p>
      <span class="read-more">Read More &gt;&gt;</span>
    </div>
    <div class="service abs" style="left:572px">
      <h2><i></i>Project Management</h2>
      <div class="service-photo" role="img" aria-label="Photo of event staff talking in a hallway" style="background:linear-gradient(170deg,#9c8d7a,#4a3e36 60%,#7a6d62)"></div>
      <p>Lorem Ipsum is simply dummy text of the printing and typesetting industry. Lorem Ipsum has been the industry's standard</p>
      <span class="read-more">Read More &gt;&gt;</span>
    </div>
  </section>

  <section class="band abs">
    <div class="offer abs" style="left:40px">
      <h3><i></i>Content Management</h3>
      <ul>
        <li>a.Speaker procurement and contracting</li>
        <li>b. Session development</li>
        <li>b. Calls for papers/presentation</li>
        <li>d. Speaker and presentation management</li>
        <li>e. Session evaluation</li>
        <li>f. Session technologies; audience response</li>
      </ul>
    </div>
    <div class="offer abs" style="left:305px">
      <h3><i></i>Event Marketing</h3>
      <ul>
        <li>a.Marketing plan development</li>
        <li>b. Printed, electronic, and web marketing</li>
        <li>c. Attendee communications</li>
        <li>d. Onsite signage and branding opportunities</li>
      </ul>
    </div>
    <div class="contact-form abs">
      <h4>Contact us</h4>
      <div class="field"><span>Name :</span><b></b></div>
      <div class="field"><span>Email :</span><b></b></div>
      <div class="field message"><span>Message :</span><b></b></div>
      <div class="send">Send &gt;&gt;</div>
    </div>
  </section>

  <footer class="footer abs">
    <div class="footer-links abs">Home &nbsp;|&nbsp; About us &nbsp;|&nbsp; Our Services &nbsp;|&nbsp; Press Room &nbsp;|&nbsp; Contact us &nbsp;|&nbsp; Sitemap</div>
    <div class="copyright abs">Copyright © 2010-2011, www.primeloomevents-demo.com</div>
  </footer>
</div>
</body>
</html>
```